little amber potatoes delicious nutritous microwave ready

we are a fresh produce packing company , the design is for microwave ready sweet potatoes . The design should include little amber microwave potatoes .Packed by Maple Hollow Growers Cedar Ridge VA 24000, US #1 Petite net weight 30 oz. remove potatoes from the bag microwave single potato on high for 4 to 5 mins. product of the USA . The potatoes will be in a clear pouch 6 inches tall by 10 inches wide

Target Market(s)

20 to 30 year old female food shopper

Industry/Entity Type

Retail

Font styles to use
Serif

Colors

Designer to choose colors to be used in the design.

Requirements
Must have
• 4 color design

```html
<!DOCTYPE html>
<html lang="en">
<head>
<meta charset="utf-8">
<title>little amber – Microwave Potatoes Label</title>
<link href="https://fonts.googleapis.com/css2?family=Lato:wght@300;400;700&display=swap" rel="stylesheet">
<style>
  :root {
    --backdrop: #f1efe9;
    --label-white: #ffffff;
    --brand-green: #3bb54a;
    --band-green: #266d37;
    --field-green-light: #37b24a;
    --field-green-dark: #119a48;
    --band-yellow: #f2ea1b;
    --badge-green: #2f7d3f;
    --badge-silver: #c9cbcf;
    --text-white: #ffffff;
  }
  * { box-sizing: border-box; margin: 0; padding: 0; }
  html, body {
    width: 1200px; height: 900px; overflow: hidden;
    background: var(--backdrop);
    font-family: "Lato", Arial, sans-serif;
  }
  .label {
    position: absolute; left: 100px; top: 150px;
    width: 1000px; height: 600px;
    background: var(--label-white);
    overflow: hidden;
    box-shadow: 0 18px 30px rgba(0,0,0,0.18);
  }
  .fields { position: absolute; inset: 0; }
  .brand-name {
    position: absolute; left: 0; right: 0; top: 38px;
    text-align: center;
    font-weight: 300; font-size: 124px; line-height: 1;
    letter-spacing: -2px;
    color: var(--brand-green);
  }
  .product-band {
    position: absolute; left: 0; top: 217px;
    width: 1000px; height: 73px;
    background: var(--band-green);
    display: flex; align-items: center; justify-content: center; gap: 28px;
  }
  .product-band .rule { width: 185px; height: 1.5px; background: var(--band-yellow); }
  .product-band h2 {
    font-weight: 300; font-size: 56px; line-height: 1;
    color: var(--band-yellow); letter-spacing: 0.5px;
  }
  .badge {
    position: absolute; top: 322px;
    width: 122px; height: 122px; border-radius: 50%;
    box-shadow: 0 3px 6px rgba(0,0,0,0.25);
  }
  .badge--local { left: 697px; background: var(--badge-green); border: 3px solid #e8efe8; }
  .badge--origin { left: 837px; background: var(--badge-silver); border: 3px solid #eeeeee; }
  .net-weight {
    position: absolute; left: 30px; top: 442px;
    display: flex; align-items: center; color: var(--text-white);
  }
  .net-weight .amount { font-weight: 300; font-size: 64px; line-height: 1; }
  .net-weight .divider { width: 2px; height: 62px; background: var(--text-white); margin: 0 14px 0 16px; }
  .net-weight .caption { font-weight: 300; font-size: 31px; line-height: 0.9; }
  .packer {
    position: absolute; left: 33px; top: 527px;
    font-weight: 300; font-size: 21px; line-height: 26px;
    color: var(--text-white);
  }
  .cooking {
    position: absolute; right: 37px; top: 470px;
    text-align: right; color: var(--text-white);
    font-size: 21px; line-height: 26.5px;
  }
  .cooking h3 { font-weight: 700; font-size: 22px; }
  .cooking p { font-weight: 300; }
</style>
</head>
<body>
  <div class="label">
    <svg class="fields" width="1000" height="600" viewBox="0 0 1000 600" aria-hidden="true">
      <defs>
        <linearGradient id="fieldLeft" x1="0" y1="0" x2="1" y2="0">
          <stop offset="0" stop-color="var(--field-green-light)"/>
          <stop offset="1" stop-color="var(--field-green-dark)"/>
        </linearGradient>
        <linearGradient id="fieldRight" x1="0" y1="0" x2="1" y2="0">
          <stop offset="0" stop-color="var(--field-green-light)"/>
          <stop offset="1" stop-color="var(--field-green-dark)"/>
        </linearGradient>
      </defs>
      <path d="M0 388 C170 386 340 420 450 545 L450 600 L0 600 Z" fill="url(#fieldLeft)"/>
      <path d="M392 600 C520 470 700 380 1000 352 L1000 600 Z" fill="url(#fieldRight)"/>
    </svg>

    <h1 class="brand-name">little amber</h1>

    <div class="product-band">
      <span class="rule"></span>
      <h2>Microwave Potatoes</h2>
      <span class="rule"></span>
    </div>

    <div class="badge badge--local" role="img" aria-label="Locally grown badge"></div>
    <div class="badge badge--origin" role="img" aria-label="Made in the USA badge"></div>

    <div class="net-weight">
      <span class="amount">30 oz</span>
      <span class="divider"></span>
      <span class="caption">Net<br>Weight</span>
    </div>

    <p class="packer">Packed by Maple Hollow Growers<br>Cedar Ridge VA 24000, US</p>

    <div class="cooking">
      <h3>How to Cook?</h3>
      <p>Remove potatoes from the<br>bag&nbsp; microwave single potato<br>on high for 4 to 5 mins.</p>
    </div>
  </div>
</body>
</html>
```